Specialised investor in e-mobility and energy wants business card design

We need a business card design that fits our existing corporate design. <The look and feel must be 'sharp'/'clean', dynamic, communicate momentum, professionalism etc (as one would imagine from a firm in the financial sector). We like the idea of a reverse-side of the card that includes the logo, and the name and contact details on the other. We expect the deliverable to be whatever format might be required to be able to get cards printed directly by a service such as tandor press. Our website is www.orm.capital

```html
<!DOCTYPE html>
<html lang="en">
<head>
<meta charset="utf-8">
<title>ORM Capital – Business Card</title>
<link href="https://fonts.googleapis.com/css2?family=Lato:wght@400;700&family=Questrial&display=swap" rel="stylesheet">
<style>
  :root{
    --backdrop:#1c1c1c;
    --card-white:#ffffff;
    --forest:#324f25;
    --leaf:#86b34a;
    --ink-light:#ffffff;
    --ink-dark:#2a4a1e;
  }
  html,body{margin:0;padding:0;width:1200px;height:1122px;overflow:hidden;background:var(--backdrop);}
  .stage{position:relative;width:1200px;height:1122px;}
  .card{position:absolute;left:220px;width:760px;height:430px;border-radius:22px;overflow:hidden;}
  .card--front{top:90px;background:var(--card-white);}
  .card--back{top:600px;background:var(--forest);}

  .wordmark{font-family:"Questrial",sans-serif;font-weight:400;color:var(--ink-dark);white-space:nowrap;}
  .card--front .wordmark{position:absolute;left:0;right:0;top:170px;text-align:center;font-size:84px;line-height:1;}
  .card--back .wordmark{position:absolute;right:48px;top:44px;font-size:52px;line-height:1;color:var(--ink-light);}

  .rule{position:absolute;height:1px;background:var(--leaf);opacity:.8;}
  .rule--main{left:300px;right:40px;top:215px;}
  .rule--contact{left:60px;width:240px;top:318px;}

  .person{position:absolute;left:60px;top:236px;font-family:"Lato",sans-serif;}
  .person__name{margin:0;font-size:30px;font-weight:700;color:var(--leaf);letter-spacing:.5px;text-transform:uppercase;}
  .person__role{margin:2px 0 0;font-size:19px;font-weight:700;color:var(--ink-light);}

  .contact{position:absolute;left:60px;top:330px;font-family:"Lato",sans-serif;font-size:16px;color:var(--ink-light);list-style:none;margin:0;padding:0;}
  .contact li{display:flex;align-items:center;gap:10px;height:24px;}
  .contact svg{width:14px;height:14px;}

  .firm{position:absolute;right:50px;top:228px;text-align:right;font-family:"Lato",sans-serif;color:var(--ink-light);}
  .firm__name{margin:0;font-size:17px;font-weight:700;}
  .firm__city{margin:2px 0 0;font-size:16px;}

  .base{position:absolute;left:0;bottom:0;width:760px;height:80px;}
  .website{position:absolute;right:42px;bottom:20px;font-family:"Lato",sans-serif;font-size:15px;color:var(--ink-dark);letter-spacing:.5px;}
</style>
</head>
<body>
<main class="stage">
  <section class="card card--front" aria-label="Card front">
    <div class="wordmark">ORM Capital</div>
  </section>

  <section class="card card--back" aria-label="Card back">
    <div class="wordmark">ORM Capital</div>
    <div class="rule rule--main"></div>

    <div class="person">
      <h1 class="person__name">Marcus Hallberg</h1>
      <p class="person__role">Founder &amp; CEO</p>
    </div>
    <div class="rule rule--contact"></div>
    <ul class="contact">
      <li><svg viewBox="0 0 16 16" aria-hidden="true"><path d="M3 1.5l2.5 0 1 3.5-1.7 1.2a8 8 0 0 0 5 5l1.2-1.7 3.5 1v2.5c0 .8-.7 1.5-1.5 1.5A13 13 0 0 1 1.5 3c0-.8.7-1.5 1.5-1.5z" fill="var(--leaf)"/></svg>+41 79 555 0148</li>
      <li><svg viewBox="0 0 16 16" aria-hidden="true"><rect x="1" y="3" width="14" height="10" fill="var(--leaf)"/><path d="M1 3l7 6 7-6" fill="none" stroke="var(--forest)" stroke-width="1.3"/></svg>marcus@orm.capital</li>
    </ul>

    <div class="firm">
      <p class="firm__name">ORM Capital S.A.</p>
      <p class="firm__city">Valbrey, Westmark</p>
    </div>

    <svg class="base" viewBox="0 0 760 80" aria-hidden="true">
      <polygon points="0,44 560,44 566,32 560,58 0,58" fill="var(--leaf)"/>
      <polygon points="0,58 560,58 578,10 760,10 760,80 0,80" fill="var(--card-white)"/>
      <polygon points="0,44 566,44 572,28 578,10 570,10 560,36 0,36" fill="var(--leaf)"/>
    </svg>
    <div class="website">www.orm.capital</div>
  </section>
</main>
</body>
</html>
```